Quietly Orchard Honey Labels

We are an importer and distributor in the UK of fine foods from Spain. We sell primarily to the retail and wholesale trade. I need a design for wrap around labels to put on jars for four different varieties of honey - Creamy Spring Blossom, Lavender, Wild Forest and Wild Thyme. The honey originates from Spain and will primarily be sold online and to independent retailers. The look and feeling I am looking for is classical, traditional, artisan and natural. I am looking for something simple and not too fussy. There needs to be an immediate obvious distinction on each label between the 4 varieties of honey, ideally by the use of different colours in some way in each design, though I would prefer the label background to be predominantly white. It is not necessary in the design to make it evident that it is from Spain. I have attached images of the jars and the honeys and also an image of the current label just for reference (but do not refer to the design). I have also attached the text for each variety of honey. The measurements for the labels are as follows: 167mm wide and 82mm high. Our logo will go on top of the lid of the jar. I really like the design I have attached to my brief. It is labelled 'Honey Design'.

Target Market(s)

Independent food retailers and online consumers

Industry/Entity Type

Fine Foods

Font styles to use
Script
Other font styles liked:
• Freeland Font for the word Honey

Requirements
Must have
• It needs to be immediately obvious by sight that each of the 4 varieties of honey are different
Nice to have
• Just the one same icon on each label for each variety of honey. Simple. Not too fussy. I really like the design attached labelled 'honey font'.

```html
<!DOCTYPE html>
<html lang="en">
<head>
<meta charset="utf-8">
<title>Quietly Orchard – Creamy Spring Blossom Honey Label</title>
<link rel="stylesheet" href="https://fonts.googleapis.com/css2?family=Cormorant+Garamond:ital,wght@0,500;0,600;1,500&display=swap">
<style>
  :root {
    --backdrop: #ecebe7;
    --label-paper: #fbf9f2;
    --gold: #d7b24a;
    --gold-soft: #e8cf7e;
    --ink: #3a2f25;
    --ink-soft: #4a3f34;
    --blossom-white: #f4f1e6;
    --blossom-yellow: #f1dd8f;
    --leaf-green: #b9c79a;
  }
  * { margin: 0; padding: 0; box-sizing: border-box; }
  html, body {
    width: 1200px;
    height: 1200px;
    overflow: hidden;
    background: var(--backdrop);
  }
  .canvas {
    position: relative;
    width: 1200px;
    height: 1200px;
  }
  .label {
    position: absolute;
    left: 120px;
    top: 130px;
    width: 960px;
    height: 940px;
    background: var(--label-paper);
    overflow: hidden;
    box-shadow: 0 2px 10px rgba(0,0,0,0.06);
  }
  .label__rules {
    position: absolute;
    inset: 0;
    width: 100%;
    height: 100%;
  }
  .floral {
    position: absolute;
  }
  .floral--left {
    left: 0;
    top: 20px;
    width: 190px;
    height: 860px;
    background: linear-gradient(180deg, var(--blossom-white) 0%, var(--blossom-yellow) 45%, var(--leaf-green) 70%, var(--blossom-white) 100%);
    opacity: 0.75;
    border-radius: 0 40px 40px 0;
  }
  .floral--right {
    right: 0;
    top: 20px;
    width: 190px;
    height: 860px;
    background: linear-gradient(180deg, var(--leaf-green) 0%, var(--blossom-white) 30%, var(--blossom-yellow) 60%, var(--blossom-white) 100%);
    opacity: 0.75;
    border-radius: 40px 0 0 40px;
  }
  .floral--bottom {
    left: 190px;
    right: 190px;
    bottom: 50px;
    height: 90px;
    background: linear-gradient(90deg, var(--blossom-white), var(--blossom-yellow) 50%, var(--blossom-white));
    opacity: 0.6;
    border-radius: 40px 40px 0 0;
  }
  .brand {
    position: absolute;
    left: 50%;
    top: 150px;
    transform: translateX(-50%);
    display: flex;
    flex-direction: column;
    align-items: center;
    gap: 10px;
  }
  .brand__circle {
    width: 120px;
    height: 120px;
    border: 3px solid var(--gold);
    border-radius: 50%;
  }
  .brand__name {
    font-family: "Cormorant Garamond", serif;
    font-weight: 600;
    font-size: 22px;
    letter-spacing: 2px;
    color: var(--gold);
    text-transform: uppercase;
  }
  .product-title {
    position: absolute;
    left: 0;
    right: 0;
    top: 420px;
    text-align: center;
    font-family: "Cormorant Garamond", serif;
    font-weight: 600;
    font-size: 64px;
    line-height: 1.15;
    letter-spacing: 1px;
    color: var(--ink);
    text-transform: uppercase;
  }
  .product-description {
    position: absolute;
    left: 215px;
    right: 215px;
    top: 640px;
    text-align: center;
    font-family: "Cormorant Garamond", serif;
    font-style: italic;
    font-weight: 500;
    font-size: 27px;
    line-height: 1.45;
    color: var(--ink-soft);
  }
</style>
</head>
<body>
<main class="canvas">
  <section class="label">
    <div class="floral floral--left" role="img" aria-label="Watercolour sprigs of white and pale yellow spring blossom with small bees"></div>
    <div class="floral floral--right" role="img" aria-label="Watercolour branches of white blossom and green leaves with small bees"></div>
    <div class="floral floral--bottom" role="img" aria-label="Row of small white spring flowers along the lower edge"></div>

    <svg class="label__rules" viewBox="0 0 960 940" aria-hidden="true">
      <line x1="0" y1="40" x2="960" y2="40" stroke="var(--gold)" stroke-width="3"/>
      <line x1="0" y1="54" x2="960" y2="54" stroke="var(--gold-soft)" stroke-width="1.5"/>
      <line x1="0" y1="870" x2="960" y2="870" stroke="var(--gold-soft)" stroke-width="1.5"/>
      <line x1="0" y1="884" x2="960" y2="884" stroke="var(--gold)" stroke-width="3"/>
    </svg>

    <div class="brand">
      <div class="brand__circle"></div>
      <span class="brand__name">Quietly Orchard</span>
    </div>

    <h1 class="product-title">Creamy<br>Spring Blossom<br>Honey</h1>

    <p class="product-description">A delightful, smooth honey with delicate floral taste from the nectar of spring flowers. Perfect for adding a touch of sweetness to tea.</p>
  </section>
</main>
</body>
</html>
```